Kelvora - Clincial terminology cross reference

We need a mobile front page and web site for a new company based in New Jersey. We develop innovative mobile applications for consumers and physicians. Our initial product Kelvora is Tro-Ven Kelvora - a cross reference between multiple clinical terminologies. We would like to see designs. We need images to show ICD9-ICD10 translation, Vurlex code translation, APP logo design and 2-3 pages in the web to sign-up and collect payments. The final design should communicate reliable and irrefutable health information. Current logo is attached.

Unlike ICD-9, ICD-10 is more descriptive and specific which means big changes for providers, coders, and billing staff alike. ‘TRO-VEN Kelvora’ helps reduce stress and increase your diagnosis coding accuracy. TRO-VEN is available on Android and iPhone platforms. The cross-reference databases are stored on the cloud and quarterly updates ensure that the information is current.

There are 3 separate versions – starter with only icd9to10 ($24.99 per year) and icd10to9, professional with 3 more features and treatments/disease info, etc.($49.99 per year), Business with all of the above, ability to create favorites list and links to genomics databases($99.99) per year.

Key features of TRO-VEN Kelvora include:

• Use a search term or ICD-10-CM code, to get mapping advise related to additional codes to be added, etc.
• Use a search term or ICD-9-CM code, to crosswalk between ICD-9-CM codes and their ICD-10-CM equivalents.
• Use a search term or ICD-10-CM code, to crosswalk between ICD-10-CM codes and their ICD-9-CM equivalents.
• Use a search term or VurLex-CM code, to crosswalk between VurLex, ICD-10-CM codes and their ICD-9-CM equivalents.
• For patients with multiple signs and symptoms treated in an encounter, determine the APG that maximizes your payments for a community clinic [Applies only to states where APG is used like New York, etc.].

To summarize, TROVEN Kelvora is a handy cross reference tool that helps providers in the ICD9-ICD10 transition efforts and continuing medical education (not used for continuing medical education in the US). The app is available on Android and iOS devices for a minimal fee and based on Volume Licenses. The App is being enhanced to provide information about treatments (clinical and diagnostic labs), medications (including medications currently in the pipeline) and diet so that it can be targeted towards patients.

Target Market(s)

healthcare providers; patients; payors

Industry/Entity Type

Healthcare

Number of Pages Required

2 page

```html
<!DOCTYPE html>
<html lang="en">
<head>
<meta charset="utf-8">
<title>Kelvora – Mobile Applications for Consumers and Physicians</title>
<link rel="stylesheet" href="https://fonts.googleapis.com/css2?family=Open+Sans:wght@400;600;700;800&family=Libre+Baskerville:wght@400;700&display=swap">
<style>
  :root{
    --blue:#1a73d9;
    --blue-dark:#1259ad;
    --sky:#25aee8;
    --ink:#1d2430;
    --text:#6b7380;
    --muted:#9aa1ab;
    --line:#e4e7eb;
    --white:#ffffff;
    --footer:#1c1e22;
    --footer-bar:#131417;
    --hero-a:#f4f7fb;
    --hero-b:#d9e4ef;
  }
  *{box-sizing:border-box;margin:0;padding:0}
  html,body{width:702px;height:1200px;overflow:hidden}
  body{font-family:"Open Sans",Arial,sans-serif;color:var(--text);background:var(--white);font-size:8px;line-height:1.5}
  .page{position:relative;width:702px;height:1200px}

  /* header */
  .site-header{height:64px;display:flex;align-items:center;justify-content:space-between;padding:0 38px 0 40px;background:var(--white)}
  .brand{display:flex;align-items:center;gap:8px;color:var(--ink);font-weight:700;font-size:14px}
  .brand-dot{width:34px;height:34px;border-radius:50%;background:var(--blue-dark)}
  .main-nav{display:flex;gap:4px}
  .main-nav a{font-size:7.5px;font-weight:600;color:var(--ink);text-decoration:none;padding:7px 9px;text-transform:uppercase}
  .main-nav a.is-active{background:var(--blue);color:var(--white)}

  /* hero */
  .hero{position:relative;height:272px;overflow:hidden}
  .hero-visual{position:absolute;inset:0;background:linear-gradient(100deg,var(--hero-a) 0%,var(--hero-a) 42%,#e8eef5 60%,var(--hero-b) 100%)}
  .hero-copy{position:relative;padding:48px 0 0 46px;width:380px}
  .hero-title{color:var(--blue);font-weight:700;font-size:19px;line-height:1.22}
  .hero-subtitle{color:var(--ink);font-weight:700;font-size:15px;margin-top:6px}
  .hero-tagline{color:var(--blue);font-weight:600;font-size:9.5px;margin-top:2px}
  .btn{display:inline-block;background:var(--blue);color:var(--white);font-size:7.5px;font-weight:600;padding:5px 12px;text-decoration:none}
  .hero .btn{margin-top:16px}
  .slider-dots{position:absolute;left:46px;bottom:28px;display:flex;gap:5px}
  .slider-dots span{width:6px;height:6px;border-radius:50%;background:#9fb6cc}
  .slider-dots span.is-current{background:var(--blue)}

  /* welcome */
  .welcome{height:142px;text-align:center;padding:32px 44px 0}
  .section-title{font-size:13px;font-weight:700;color:var(--ink);text-transform:uppercase;letter-spacing:.2px}
  .welcome p{margin-top:12px;font-size:7.5px;line-height:1.65}

  /* product band */
  .product-band{height:142px;background:var(--blue);display:grid;grid-template-columns:1fr 150px 1fr;color:var(--white)}
  .product-col{padding:22px 24px 0 46px}
  .product-col.right{padding:22px 46px 0 20px}
  .product-col h2{font-size:13px;font-weight:700;text-transform:uppercase}
  .product-col p{margin-top:6px;font-size:7.5px;line-height:1.6;color:#dce9fb}
  .product-col .btn{margin-top:10px;background:var(--blue-dark)}
  .product-visual{background:linear-gradient(180deg,#2a85e6,#0f4c96);margin:0 10px}

  /* what we do */
  .what-we-do{height:186px;text-align:center;padding:18px 44px 0}
  .what-we-do > p{margin-top:10px;font-size:7.5px;line-height:1.7;padding:0 20px}
  .services{display:grid;grid-template-columns:1fr 1fr;gap:26px;margin-top:14px;text-align:left}
  .service-card{display:flex;gap:12px}
  .service-visual{flex:0 0 116px;height:84px;background:linear-gradient(135deg,#dfe6ee,#b9c7d6)}
  .service-card h3{color:var(--blue);font-size:11px;font-weight:700}
  .service-card p{font-size:7.5px;line-height:1.6;margin-top:3px}
  .read-link{display:inline-block;margin-top:5px;color:var(--ink);font-weight:700;font-size:7.5px;text-decoration:none}

  /* blog */
  .blog{position:relative;height:138px;background:var(--sky);color:var(--white);text-align:center;padding:26px 70px 0}
  .blog .section-title{color:var(--white)}
  .blog p{margin-top:10px;font-size:7.5px;line-height:1.7}
  .blog-meta{margin-top:8px;font-size:7.5px}
  .blog-meta strong{display:block;font-weight:700}
  .blog-arrow{position:absolute;top:58px;width:16px;height:16px}
  .blog-arrow.prev{left:34px}
  .blog-arrow.next{right:34px}

  /* featured */
  .featured{height:62px;text-align:center;padding-top:10px}
  .featured .section-title{font-size:12px}
  .press-list{display:flex;justify-content:center;align-items:center;gap:26px;margin-top:9px;color:#3a3f47}
  .press-list span{font-family:"Libre Baskerville",Georgia,serif;font-size:10px;font-weight:700}

  /* footer */
  .site-footer{height:170px;background:var(--footer);display:grid;grid-template-columns:190px 1fr 1fr;gap:30px;padding:22px 40px 0 36px;color:#a4a9b1}
  .site-footer h4{color:var(--white);font-size:12px;font-weight:700;text-transform:uppercase}
  .site-footer h5{color:var(--blue);font-size:9px;font-weight:700;text-transform:uppercase}
  .news-date{color:var(--blue);font-weight:700;font-size:8px;margin-top:8px}
  .news-text{color:#c9ccd1;font-size:7.5px;line-height:1.6;margin-top:2px}
  .news-link{display:inline-block;color:var(--white);font-weight:700;font-size:7.5px;margin-top:8px;text-decoration:none}
  .footer-links{list-style:none;margin-top:10px;font-size:7px;text-transform:uppercase}
  .footer-links li{padding:4px 0;border-bottom:1px solid #2c2f35}
  .footer-links.two-col{display:grid;grid-template-columns:1fr 1fr;column-gap:18px}

  .footer-bar{height:24px;background:var(--footer-bar);display:flex;align-items:center;justify-content:space-between;padding:0 38px 0 36px;color:#7e848c;font-size:6.5px}
  .social{display:flex;gap:4px}
  .social span{width:10px;height:10px;border:1px solid #6b7078}
</style>
</head>
<body>
<div class="page">

  <header class="site-header">
    <div class="brand"><span class="brand-dot"></span>Kelvora</div>
    <nav class="main-nav">
      <a class="is-active" href="#">Home</a>
      <a href="#">About Us</a>
      <a href="#">Product</a>
      <a href="#">Services &amp; Support</a>
      <a href="#">Client</a>
      <a href="#">Blog</a>
      <a href="#">Contact Us</a>
    </nav>
  </header>

  <section class="hero">
    <div class="hero-visual" role="img" aria-label="Photo of a physician in a white coat holding a smartphone showing the app"></div>
    <div class="hero-copy">
      <h1 class="hero-title">We Develop Innovative Mobile Applications for Consumers and Physicians.</h1>
      <p class="hero-subtitle">Our Initial Product Tro-Ven Kelvora</p>
      <p class="hero-tagline">A cross reference between multiple clinical terminologies.</p>
      <a class="btn" href="#">Read More</a>
    </div>
    <div class="slider-dots"><span class="is-current"></span><span></span><span></span><span></span></div>
  </section>

  <section class="welcome">
    <h2 class="section-title">Welcome to Our Website</h2>
    <p>Our team builds reliable clinical tools that help providers, coders and billing staff find accurate answers quickly. Every reference is reviewed by specialists and kept current through regular quarterly updates stored securely in the cloud. We listen to the people who use our apps each day and shape every release around their needs, so the information you rely on stays clear, trusted and easy to reach from any device. From small community clinics to large practices, our tools support better coding, fewer denied claims and more time for patient care, while new features for treatments, medications and diet continue to grow with every release we ship.</p>
  </section>

  <section class="product-band">
    <div class="product-col">
      <h2>Our Product</h2>
      <p>Tro-Ven Kelvora gives providers a fast crosswalk between coding systems on any phone or tablet. Search by term or code and get clear mapping advice in seconds.</p>
    </div>
    <div class="product-visual" role="img" aria-label="Photo of a hand holding a smartphone displaying the Kelvora app"></div>
    <div class="product-col right">
      <h2>Tro-Ven Kelvora</h2>
      <p>Translate ICD-9 to ICD-10 and back, map Vurlex codes and reduce stress around diagnosis coding with one handy reference tool.</p>
      <a class="btn" href="#">Read More</a>
    </div>
  </section>

  <section class="what-we-do">
    <h2 class="section-title">What We Do</h2>
    <p>We design mobile applications that turn complex clinical terminology into simple answers for patients, providers and payors. Our work joins careful medical review with clean design so every screen feels calm and dependable.</p>
    <div class="services">
      <article class="service-card">
        <div class="service-visual" role="img" aria-label="Photo of a family looking at a tablet together"></div>
        <div>
          <h3>Consumers</h3>
          <p>Clear information on treatments, medications and diet helps patients understand their care and talk with confidence.</p>
          <a class="read-link" href="#">Read More</a>
        </div>
      </article>
      <article class="service-card">
        <div class="service-visual" role="img" aria-label="Photo of a physician reviewing notes on a clipboard"></div>
        <div>
          <h3>Physicians</h3>
          <p>Accurate code crosswalks and mapping advice help physicians and staff bill correctly and save time each day.</p>
          <a class="read-link" href="#">Read More</a>
        </div>
      </article>
    </div>
  </section>

  <section class="blog">
    <svg class="blog-arrow prev" viewBox="0 0 16 16" aria-hidden="true"><path d="M10 3 L5 8 L10 13" fill="none" stroke="#fff" stroke-width="1.6"/></svg>
    <h2 class="section-title">Blog Posts</h2>
    <p>Read our latest notes on the ICD-10 transition, coding accuracy and new features arriving in the next quarterly update of the app. Our specialists share practical tips for coders and billing staff, answers to common questions from clinics, and short guides that make every change easier to follow.</p>
    <div class="blog-meta"><strong>Company Name</strong>Posted Date</div>
    <svg class="blog-arrow next" viewBox="0 0 16 16" aria-hidden="true"><path d="M6 3 L11 8 L6 13" fill="none" stroke="#fff" stroke-width="1.6"/></svg>
  </section>

  <section class="featured">
    <h2 class="section-title">As Featured On</h2>
    <div class="press-list">
      <span>Harbor Ledger</span>
      <span>Northwind</span>
      <span>QTV</span>
      <span>Market Courier</span>
      <span>CodeCrate</span>
      <span>Coastline Times</span>
    </div>
  </section>

  <footer class="site-footer">
    <div>
      <h4>Latest News</h4>
      <p class="news-date">Jul 28 2016</p>
      <p class="news-text">Quarterly database update now live for all starter, professional and business plans.</p>
      <a class="news-link" href="#">Learn More</a>
    </div>
    <div>
      <h5>Company</h5>
      <ul class="footer-links two-col">
        <li>Home</li><li>Client</li>
        <li>About Us</li><li>Blog</li>
        <li>Product</li><li>Contact Us</li>
        <li>Services &amp; Support</li><li>&nbsp;</li>
      </ul>
    </div>
    <div>
      <h5>Services &amp; Support</h5>
      <ul class="footer-links">
        <li>ICD9 to ICD10</li>
        <li>ICD10 to ICD9</li>
        <li>Vurlex Mapping</li>
        <li>APG Payments</li>
      </ul>
    </div>
  </footer>
  <div class="footer-bar">
    <span>© 2016 Company Name. All rights reserved.</span>
    <div class="social"><span></span><span></span><span></span><span></span></div>
  </div>

</div>
</body>
</html>
```